Global Yoga Apparel Brand Needs a Beautiful Website

We need a website design for a new Yoga brand called Vessa. We develop beautiful, stylish, sexy, comfortable yoga leggings, tops, and yoga apparel for women looking to feel their best, look their best and perform their best on and off the yoga mat.
This will go up at http://vessa.example/ (which is a landing page right now).
We would like to see simple and clean design where the focus will be on powerful images and clean background space. We will be using Shopify to start building on and here are three sites that we would love to see options based off of the look, layout and feel while making something unique at the same time:
1. Tumo.ca
2. marikoven.com
3. www.q-plume.com
The final design should look clean, beautiful, inspiring, powerful and empowering.
Target Market(s)
mostly Females 21-35 range but will be appealing to women over 35 as well.

```html
<!DOCTYPE html>
<html lang="en">
<head>
<meta charset="utf-8">
<title>Vessa — Yoga Apparel</title>
<link href="https://fonts.googleapis.com/css2?family=Montserrat:wght@400;500;600;700&display=swap" rel="stylesheet">
<style>
:root{
  --ink:#1f1f1f;
  --muted:#6b6b6b;
  --line:#e4e4e4;
  --accent:#dd9a12;
  --purple:#a70fd5;
  --teal:#15b6b2;
  --amber:#e09c0b;
  --rose:#e8375c;
  --band:#f1f1f1;
  --white:#fff;
}
*{box-sizing:border-box;margin:0;padding:0}
html,body{width:1200px;height:3557px;overflow:hidden}
body{font-family:"Montserrat",Arial,sans-serif;color:var(--ink);background:var(--white);position:relative}
a{color:inherit;text-decoration:none}

/* header */
.site-header{height:178px;position:relative;border-bottom:1px solid var(--line)}
.brand{position:absolute;left:0;right:0;top:30px;text-align:center;font-size:52px;font-weight:700;letter-spacing:1px;line-height:1}
.header-tools{position:absolute;right:148px;top:62px;display:flex;gap:26px;align-items:center}
.cart{position:relative}
.cart-count{position:absolute;top:-16px;right:-12px;width:20px;height:20px;border-radius:50%;background:#eee;font-size:10px;display:flex;align-items:center;justify-content:center;color:var(--muted)}
.main-nav{position:absolute;top:132px;left:0;right:0;display:flex;justify-content:center;gap:0}
.main-nav a{font-size:14px;font-weight:500;letter-spacing:.5px;padding:0 34px;position:relative;height:32px}
.main-nav a.active::after{content:"";position:absolute;left:34px;right:34px;bottom:0;height:3px;background:var(--accent)}

/* hero */
.hero{height:446px;position:relative;background:linear-gradient(90deg,#ececec 0%,#e6e6e6 55%,#d4d7df 100%)}
.hero-photo{position:absolute;left:520px;top:0;right:0;bottom:0;background:radial-gradient(ellipse at 55% 40%,#6a7a98 0%,#8a95ab 30%,rgba(220,222,228,0) 70%)}
.hero-copy{position:absolute;left:135px;top:128px}
.hero-copy h1{font-size:44px;font-weight:600;line-height:1.1;letter-spacing:.5px;color:#2a2a2a}
.hero-copy h2{font-size:32px;font-weight:500;color:#4a4a4a;margin-top:6px}
.btn-solid{display:inline-block;background:var(--accent);color:var(--white);font-size:13px;font-weight:600;padding:12px 22px;letter-spacing:.5px}
.hero-copy .btn-solid{margin-top:26px}
.dots{display:flex;gap:6px;margin-top:30px}
.dots span{width:14px;height:14px;border-radius:50%;background:#999;border:2px solid #ccc}
.dots span:first-child{background:#fff}

/* promo grid */
.promo-grid{display:grid;grid-template-columns:600px 600px;grid-template-rows:243px 243px}
.promo{position:relative;color:var(--white);padding:80px 0 0 132px}
.promo h3{font-size:24px;font-weight:500;line-height:1;text-transform:uppercase}
.promo h3 strong{display:block;font-size:34px;font-weight:600;margin-top:4px}
.btn-outline{display:inline-block;border:2px solid var(--white);color:var(--white);font-size:11px;font-weight:600;padding:6px 16px;margin-top:14px}
.promo-1{background:linear-gradient(120deg,#8a4a36,#6b2f4f 60%,#b2337a)}
.promo-2{background:linear-gradient(120deg,#e2368a,#b34bc9 60%,#2c2c2c)}
.promo-3{background:linear-gradient(120deg,#2d3f5c,#5d6f8c 50%,#c2267a)}
.promo-4{background:linear-gradient(120deg,#f2a41c,#f58f2a 55%,#7dd7c4)}

/* product sections */
.section-title{font-size:20px;font-weight:600;text-align:center;letter-spacing:.5px}
.arrows{display:flex;gap:8px}
.arrows span{width:28px;height:28px;border:1px solid var(--line);display:flex;align-items:center;justify-content:center}
.featured{height:512px;position:relative}
.featured .section-title{position:absolute;top:40px;left:0;right:0}
.featured .arrows{position:absolute;right:135px;top:40px}
.product-row{position:absolute;left:135px;right:135px;display:flex;justify-content:space-between}
.featured .product-row{top:95px}
.product{width:228px;text-align:center;padding-bottom:12px}
.product-img{height:235px;position:relative;display:flex;align-items:center;justify-content:center}
.product.hover{background:#e4e4e4}
.product .name{font-size:14px;font-weight:600;margin-top:20px}
.product .price{font-size:24px;font-weight:600;color:var(--accent);margin-top:6px}
.stars{font-size:13px;color:var(--accent);letter-spacing:2px;margin-top:4px}
.stars .off{color:#bbb}
.add-cart{border:2px solid var(--white);color:var(--white);font-size:12px;font-weight:600;padding:8px 18px}

.deal-banner{height:316px;position:relative;background:linear-gradient(90deg,#5a3a6e 0%,#4a2e2a 35%,#5a3a28 70%,#3a2a22 100%)}
.deal-banner .copy{position:absolute;left:160px;top:76px;color:var(--white)}
.deal-banner h3{font-size:40px;font-weight:600;line-height:1.2}
.deal-banner h3 em{font-style:normal;color:#ffd200}
.deal-banner .btn-outline{margin-top:30px;font-size:13px;padding:8px 20px}

.lists{height:510px;position:relative}
.list-head{position:absolute;top:52px;display:flex;align-items:center;gap:60px}
.list-head .section-title{font-size:20px}
.list-head.latest{left:330px}
.list-head.sale{left:782px}
.lists .product-row{top:130px}

/* category tiles */
.tiles{display:flex;height:240px}
.tile{flex:1;position:relative;color:var(--white);display:flex;flex-direction:column;align-items:center;justify-content:center}
.tile h4{font-size:28px;font-weight:600}
.tile p{font-size:15px;font-weight:500;margin-top:6px}
.tile-1{background:linear-gradient(120deg,#4f6e62,#a08a6e 60%,#8a6a55)}
.tile-2{background:linear-gradient(120deg,#3a4660,#5c6a80 45%,#b23a6e)}
.tile-3{background:linear-gradient(120deg,#2b6aa8,#e2d83a 55%,#d8e04a)}
.tile-3 h4,.tile-3 p{color:#fff}

/* partners */
.partners{height:147px;display:flex;align-items:center;justify-content:center;gap:62px;color:#7a7a7a}
.partners .mark{font-size:26px;font-weight:600;letter-spacing:.5px}
.partners .chev{font-size:30px;color:#555}

/* perks */
.perks{display:flex;height:225px;color:var(--white);text-align:center}
.perk{display:flex;flex-direction:column;align-items:center;justify-content:center;padding:0 30px;position:relative}
.perk h5{font-size:21px;font-weight:600;line-height:1.2;text-transform:uppercase}
.perk p{font-size:10px;line-height:1.5;margin-top:10px;max-width:200px}
.perk .glyph{position:absolute;top:36px;left:50%;transform:translateX(-50%);opacity:.25}
.perk-1{width:363px;background:var(--purple)}
.perk-2{width:237px;background:var(--teal)}
.perk-3{width:237px;background:var(--amber)}
.perk-4{width:363px;background:var(--rose)}

/* newsletter */
.newsletter{height:119px;background:var(--band);display:flex;align-items:center;justify-content:center}
.signup{display:flex;width:636px;height:47px;background:var(--white);border:1px solid var(--line)}
.signup label{font-size:13px;font-weight:600;padding:0 16px;display:flex;align-items:center;white-space:nowrap}
.signup .field{flex:1;font-size:11px;color:#aaa;display:flex;align-items:center}
.signup .submit{background:var(--accent);color:var(--white);font-size:13px;font-weight:600;width:136px;display:flex;align-items:center;justify-content:center}

/* footer */
.site-footer{height:378px;position:relative}
.footer-cols{position:absolute;top:62px;left:135px;display:flex}
.footer-col h6{font-size:14px;font-weight:600;color:var(--accent);letter-spacing:.5px;margin-bottom:22px}
.footer-col li{list-style:none;font-size:12px;color:var(--muted);line-height:24px}
.col-a{width:216px}.col-b{width:249px}.col-c{width:221px}
.contact li{display:flex;align-items:flex-start;gap:10px}
.socials{display:flex;gap:22px;margin-top:20px}
.socials span{width:18px;height:18px;border-radius:50%;background:#555}
.legal{position:absolute;left:135px;right:135px;top:320px;border-top:1px solid var(--line);padding-top:22px;text-align:center;font-size:11px;color:#999}
</style>
</head>
<body>

<header class="site-header">
  <div class="brand">Vessa</div>
  <div class="header-tools">
    <svg width="18" height="18" viewBox="0 0 18 18"><circle cx="7.5" cy="7.5" r="5.5" fill="none" stroke="#222" stroke-width="2"/><line x1="11.5" y1="11.5" x2="16" y2="16" stroke="#222" stroke-width="2"/></svg>
    <svg width="18" height="18" viewBox="0 0 18 18"><circle cx="9" cy="5" r="4" fill="#222"/><path d="M1 18c0-5 3.5-7 8-7s8 2 8 7z" fill="#222"/></svg>
    <span class="cart">
      <svg width="26" height="22" viewBox="0 0 26 22"><path d="M1 3h4l3 12h13l3-9H7" fill="#1a9e3a"/><circle cx="10" cy="19" r="2" fill="#1a9e3a"/><circle cx="19" cy="19" r="2" fill="#1a9e3a"/></svg>
      <span class="cart-count">0</span>
    </span>
  </div>
  <nav class="main-nav">
    <a class="active">HOME</a><a>ABOUT US</a><a>PRODUCTS</a><a>TOP SELLING</a><a>SHOP NOW</a><a>BLOG</a><a>RESOURCES</a>
  </nav>
</header>

<section class="hero">
  <div class="hero-photo" role="img" aria-label="Woman in a blue top and grey leggings in a wide-legged forward bend"></div>
  <div class="hero-copy">
    <h1>VESSA YOGA TOPS</h1>
    <h2>AND LEGGINGS</h2>
    <a class="btn-solid">SHOP NOW</a>
    <div class="dots"><span></span><span></span><span></span><span></span></div>
  </div>
</section>

<section class="promo-grid">
  <div class="promo promo-1" role="img" aria-label="Woman seated in purple patterned leggings against a brick wall"><h3>Comfort Yoga<strong>Leggings</strong></h3><a class="btn-outline">SHOP NOW</a></div>
  <div class="promo promo-2" role="img" aria-label="Sneakers and water bottle on a bright pink surface"><h3>Special Coupon<strong>Discount</strong></h3><a class="btn-outline">SHOP NOW</a></div>
  <div class="promo promo-3" role="img" aria-label="Folded yoga tops and denim on a wooden floor"><h3>Special Yoga<strong>Tops is here</strong></h3><a class="btn-outline">SHOP NOW</a></div>
  <div class="promo promo-4" role="img" aria-label="Legs in mint leggings and pink trainers on an orange background"><h3>Top Brands<strong>Materials</strong></h3><a class="btn-outline">SHOP NOW</a></div>
</section>

<section class="featured">
  <h2 class="section-title">FEATURED PRODUCTS</h2>
  <div class="arrows"><span>‹</span><span>›</span></div>
  <div class="product-row">
    <div class="product"><div class="product-img" role="img" aria-label="Pink sports bra and black shorts" style="background:linear-gradient(#f3f3f3,#e8c7cf)"></div><p class="name">PRODUCT NAME</p><p class="price">$65.00</p><p class="stars">★★★★★</p></div>
    <div class="product hover"><div class="product-img" role="img" aria-label="Dark yoga jacket" style="background:linear-gradient(#3a3a3a,#1e1e1e)"><span class="add-cart">ADD TO CART</span></div><p class="name">PRODUCT NAME</p><p class="price">$45.00</p><p class="stars">★★★★★</p></div>
    <div class="product"><div class="product-img" role="img" aria-label="White and black leggings" style="background:linear-gradient(90deg,#f4f2ee 50%,#2a2a2a 50%)"></div><p class="name">PRODUCT NAME</p><p class="price">$60.00</p><p class="stars">★★★★<span class="off">★</span></p></div>
    <div class="product"><div class="product-img" role="img" aria-label="Floral print leggings with dumbbells" style="background:linear-gradient(135deg,#2b2233,#b43f8d 55%,#8e7bd0)"></div><p class="name">PRODUCT NAME</p><p class="price">$75.00</p><p class="stars">★★★★★</p></div>
  </div>
</section>

<section class="deal-banner" role="img" aria-label="Purple yoga mat, earphones, phone, striped top and white sneakers on wood">
  <div class="copy">
    <h3>BUY 3 AND GET 1 <em>FREE</em><br>FROM US</h3>
    <a class="btn-outline">SHOP NOW</a>
  </div>
</section>

<section class="lists">
  <div class="list-head latest"><h2 class="section-title">LATEST</h2><div class="arrows"><span>‹</span><span>›</span></div></div>
  <div class="list-head sale"><h2 class="section-title">ON SALE</h2><div class="arrows"><span>‹</span><span>›</span></div></div>
  <div class="product-row">
    <div class="product"><div class="product-img" role="img" aria-label="Patterned leggings with camera and sneakers" style="background:linear-gradient(135deg,#c44f9a,#e6d6e8 50%,#2b2b2b)"></div><p class="name">PRODUCT NAME</p><p class="price">$65.00</p><p class="stars">★★★★★</p></div>
    <div class="product"><div class="product-img" role="img" aria-label="Bright top and orange shorts flat lay" style="background:linear-gradient(#b03fb8,#ff7a2a 60%,#e9e9e9)"></div><p class="name">PRODUCT NAME</p><p class="price">$45.00</p><p class="stars">★★★★★</p></div>
    <div class="product"><div class="product-img" role="img" aria-label="Black capri leggings with pink waistband" style="background:linear-gradient(#f3f3f3,#222 30%,#1a1a1a)"></div><p class="name">PRODUCT NAME</p><p class="price">$60.00</p><p class="stars">★★★★<span class="off">★</span></p></div>
    <div class="product"><div class="product-img" role="img" aria-label="Grey sports bra and folded tee" style="background:linear-gradient(135deg,#3a3d44,#7d8088)"></div><p class="name">PRODUCT NAME</p><p class="price">$75.00</p><p class="stars">★★★★★</p></div>
  </div>
</section>

<section class="tiles">
  <div class="tile tile-1" role="img" aria-label="Rolled yoga mat outdoors"><h4>YOGA MAT</h4><p>GET 20% OFF NOW</p></div>
  <div class="tile tile-2" role="img" aria-label="Yoga apparel flat lay on denim"><h4>YOGA APPAREL</h4><p>LATEST COLLECTIONS</p></div>
  <div class="tile tile-3" role="img" aria-label="Yellow mat and sneakers on blue boards"><h4>TOP SELLS</h4><p>SPECIAL DEALS</p></div>
</section>

<section class="partners">
  <span class="chev">‹</span>
  <span class="mark">KESTRO</span>
  <span class="mark">Aulmera</span>
  <span class="mark">TORVANE</span>
  <span class="mark">Nelvari</span>
  <span class="mark">fennel</span>
  <span class="mark">BRISKO</span>
  <span class="chev">›</span>
</section>

<section class="perks">
  <div class="perk perk-1">
    <svg class="glyph" width="60" height="60" viewBox="0 0 60 60"><path d="M8 8h24l20 20-24 24L8 32z" fill="#fff"/></svg>
    <h5>Special<br>Discounts</h5><p>ultrices orci ac feugiat suscipit leo massa sodales scelerisque</p>
  </div>
  <div class="perk perk-2">
    <svg class="glyph" width="60" height="60" viewBox="0 0 60 60"><path d="M10 40c0-16 12-24 26-24V6l18 18-18 18V30c-12 0-20 4-26 10z" fill="#fff"/></svg>
    <h5>7 Days Order<br>Return</h5><p>ultrices orci ac feugiat suscipit leo massa sodales scelerisque</p>
  </div>
  <div class="perk perk-3">
    <svg class="glyph" width="60" height="60" viewBox="0 0 60 60"><rect x="6" y="12" width="48" height="36" fill="#fff"/></svg>
    <h5>Free<br>Shipping</h5><p>ultrices orci ac feugiat suscipit leo massa sodales scelerisque</p>
  </div>
  <div class="perk perk-4">
    <svg class="glyph" width="60" height="60" viewBox="0 0 60 60"><rect x="6" y="16" width="48" height="28" fill="#fff"/></svg>
    <h5>Cash on<br>Delivery</h5><p>ultrices orci ac feugiat suscipit leo massa sodales scelerisque</p>
  </div>
</section>

<section class="newsletter">
  <div class="signup">
    <label>NEWSLETTER SIGN UP</label>
    <span class="field">Your Email</span>
    <span class="submit">SUBSCRIBE</span>
  </div>
</section>

<footer class="site-footer">
  <div class="footer-cols">
    <div class="footer-col col-a"><h6>INFORMATION</h6><ul><li>About Us</li><li>Customer Service</li><li>Privacy Policy</li><li>Site Map</li><li>Search Terms</li><li>Advanced Search</li><li>Orders and Returns</li></ul></div>
    <div class="footer-col col-b"><h6>WHY BUY FROM US</h6><ul><li>Shipping &amp; Returns</li><li>Secure Shopping</li><li>International Shipping</li><li>Affiliates</li><li>Group Sales</li></ul></div>
    <div class="footer-col col-c"><h6>MY ACCOUNT</h6><ul><li>Sign In</li><li>View Cart</li><li>My Wishlist</li><li>Track My Order</li><li>Help</li></ul></div>
    <div class="footer-col contact"><h6>CONTACT US</h6>
      <ul>
        <li><svg width="12" height="16" viewBox="0 0 12 16" style="margin-top:4px"><path d="M6 0a6 6 0 0 1 6 6c0 4-6 10-6 10S0 10 0 6a6 6 0 0 1 6-6z" fill="#555"/><circle cx="6" cy="6" r="2" fill="#fff"/></svg><span style="line-height:16px;padding-top:4px">214 Linden Court Suite B12<br>Marlow, PA 19350</span></li>
        <li><svg width="12" height="12" viewBox="0 0 12 12" style="margin-top:6px"><path d="M2 0l3 3-1.5 2a7 7 0 0 0 3.5 3.5L9 7l3 3-2 2C5 12 0 7 0 2z" fill="#555"/></svg>(555) 014-2280</li>
        <li><svg width="14" height="10" viewBox="0 0 14 10" style="margin-top:7px"><rect width="14" height="10" fill="#555"/><path d="M0 0l7 5 7-5" fill="none" stroke="#fff"/></svg>info@vessa.example</li>
      </ul>
      <div class="socials"><span></span><span></span><span></span><span></span></div>
    </div>
  </div>
  <div class="legal">© 2016 Company Name. All right reserved  Term of Use</div>
</footer>

</body>
</html>
```